Homvuk Business Card Project showing the logo and a bellan image on the rear

Design a whacky but professional business card, the logo is for the front and the Bellan image is for the rear. Happy to consider other open source Bellan Images if the designer wants to select one from the web. Homvuk is a competitor to TKU.com.au and Parcelo.com.au and is based around every property in Australia

Target Market(s)

Business

Contact Information for Business Card

Name, Title, Email, Web, Phone Number

Font styles to use
Other font styles liked:
• avenir

Requirements
Must have
• Image on Back logo on front
Nice to have
• Happy to consider other images on rear, preftably Oskar Bellan. Image supplied I own, we can use open source other Bellan Images

```html
<!DOCTYPE html>
<html lang="en">
<head>
<meta charset="utf-8">
<title>Homvuk Business Card</title>
<link href="https://fonts.googleapis.com/css2?family=Montserrat:wght@400;500;700;800&display=swap" rel="stylesheet">
<style>
  :root {
    --orange: #f7931e;
    --ink: #1c1c1c;
    --card-white: #ffffff;
    --card-dark: #1e1e1e;
    --backdrop: #2b2b2b;
    --muted: #2a2a2a;
  }
  * { margin: 0; padding: 0; box-sizing: border-box; }
  html, body { width: 1200px; height: 900px; overflow: hidden; }
  body {
    background: var(--backdrop);
    font-family: "Montserrat", sans-serif;
    display: flex;
    flex-direction: column;
    align-items: center;
    justify-content: center;
    gap: 56px;
  }
  .card {
    position: relative;
    width: 640px;
    height: 366px;
    overflow: hidden;
    box-shadow: 0 14px 30px rgba(0,0,0,0.45);
  }

  /* Front */
  .card-front { background: var(--card-white); }
  .brand {
    position: absolute;
    left: 48px;
    top: 44px;
    display: flex;
    align-items: center;
    gap: 12px;
  }
  .brand-square {
    width: 22px;
    height: 22px;
    background: var(--orange);
  }
  .brand-name {
    font-weight: 800;
    font-size: 40px;
    color: var(--ink);
    letter-spacing: 0.5px;
  }
  .divider {
    position: absolute;
    left: 48px;
    right: 40px;
    top: 206px;
    height: 1.5px;
    background: var(--orange);
  }
  .person {
    position: absolute;
    right: 40px;
    top: 150px;
    text-align: right;
  }
  .person-name {
    font-weight: 500;
    font-size: 22px;
    color: var(--orange);
    letter-spacing: 1px;
    text-transform: uppercase;
  }
  .person-title {
    font-size: 16px;
    color: var(--ink);
    margin-top: 2px;
  }
  .contacts {
    position: absolute;
    left: 48px;
    top: 222px;
    list-style: none;
    font-size: 14px;
    color: var(--ink);
  }
  .contacts li {
    display: flex;
    align-items: center;
    gap: 8px;
    line-height: 22px;
  }
  .contacts svg { width: 12px; height: 12px; flex: none; }
  .band {
    position: absolute;
    left: 0;
    bottom: 0;
    width: 640px;
    height: 72px;
  }

  /* Back */
  .card-back {
    background: var(--card-dark);
    display: flex;
    align-items: center;
    justify-content: center;
    gap: 18px;
  }
  .card-back .brand-square { width: 40px; height: 40px; }
  .card-back .brand-name {
    font-size: 84px;
    color: #ffffff;
  }
</style>
</head>
<body>

  <section class="card card-front" aria-label="Business card front">
    <div class="brand">
      <span class="brand-square"></span>
      <span class="brand-name">Homvuk</span>
    </div>

    <div class="person">
      <p class="person-name">Dana Corliss</p>
      <p class="person-title">Director</p>
    </div>

    <div class="divider"></div>

    <ul class="contacts">
      <li>
        <svg viewBox="0 0 12 12"><path d="M3 1 L5 3.5 L4 5 Q5.5 7.5 7 8 L8.5 7 L11 9 L9.5 11 Q4 10.5 1 3 Z" fill="#f7931e"/></svg>
        555-014-2290
      </li>
      <li>
        <svg viewBox="0 0 12 12"><rect x="1" y="2.5" width="10" height="7" fill="none" stroke="#f7931e" stroke-width="1.2"/><path d="M1 2.5 L6 6.5 L11 2.5" fill="none" stroke="#f7931e" stroke-width="1.2"/></svg>
        info@homvuk.com.au
      </li>
      <li>
        <svg viewBox="0 0 12 12"><circle cx="6" cy="6" r="5" fill="none" stroke="#f7931e" stroke-width="1.1"/><path d="M1 6 H11 M6 1 V11 M2.2 3.5 H9.8 M2.2 8.5 H9.8" stroke="#f7931e" stroke-width="0.8" fill="none"/></svg>
        www.homvuk.com.au
      </li>
    </ul>

    <svg class="band" viewBox="0 0 640 72" preserveAspectRatio="none" aria-hidden="true">
      <path d="M0 6 L250 40 Q262 42 270 46 L0 46 Z" fill="#1c1c1c"/>
      <path d="M0 14 L260 48 Q300 52 330 62 L360 72 L0 72 Z" fill="#f7931e"/>
      <path d="M260 48 Q300 52 330 62 L360 72 L640 72 L640 72 L360 72 Z" fill="#f7931e"/>
      <path d="M250 72 L640 72 L640 60 L470 60 Z" fill="#f7931e"/>
    </svg>
    <div style="position:absolute;right:0;top:198px;width:10px;height:18px;background:var(--orange);"></div>
  </section>

  <section class="card card-back" aria-label="Business card back">
    <span class="brand-square"></span>
    <span class="brand-name">Homvuk</span>
  </section>

</body>
</html>
```